Corvane Supplies Business Card

Professional business card that stand out to our potential customers. Front and back with clean modern design

Industry/Entity Type

Oil and gas

Contact Information for Business Card

Name, address, website , office phone and cell number

Requirements
Must have
• Editable files for each employee

```html
<!DOCTYPE html>
<html lang="en">
<head>
<meta charset="utf-8">
<title>Corvane Supplies Business Card</title>
<link rel="stylesheet" href="https://fonts.googleapis.com/css2?family=Montserrat:wght@400;500;700&display=swap">
<style>
  :root {
    --bg: #3a3b3d;
    --card-white: #ffffff;
    --card-black: #1b1b1c;
    --brand-red: #ee1c1c;
    --brand-cyan: #1fb3d1;
    --ink: #1e1e1e;
    --paper-text: #ffffff;
  }
  * { margin: 0; padding: 0; box-sizing: border-box; }
  html, body {
    width: 1200px; height: 1200px; overflow: hidden;
    background: var(--bg);
    font-family: "Montserrat", sans-serif;
  }
  .sheet {
    position: relative; width: 1200px; height: 1200px;
    display: flex; flex-direction: column; align-items: center; justify-content: center; gap: 52px;
  }
  .card {
    position: relative; width: 900px; height: 514px;
    border-radius: 40px; overflow: hidden;
    box-shadow: 0 3px 0 var(--brand-red), 0 18px 40px rgba(0,0,0,.45);
  }
  .card--front { background: var(--card-white); }
  .card--back { background: var(--card-black); }

  .brand {
    position: absolute; display: flex; align-items: center; gap: 14px;
    font-weight: 700; text-transform: uppercase; letter-spacing: .04em;
    color: var(--brand-red); white-space: nowrap;
  }
  .brand__square { background: var(--brand-red); flex: none; }
  .card--front .brand { left: 470px; top: 120px; font-size: 34px; }
  .card--front .brand__square { width: 28px; height: 28px; }
  .card--back .brand { left: 50%; top: 50%; transform: translate(-50%, -50%); font-size: 52px; }
  .card--back .brand__square { width: 44px; height: 44px; }

  .person { position: absolute; left: 80px; top: 250px; }
  .person__name { font-weight: 700; font-size: 44px; color: var(--brand-red); line-height: 1; letter-spacing: .01em; }
  .person__role { font-weight: 400; font-size: 30px; color: var(--ink); line-height: 1.1; margin-top: 4px; }

  .divider {
    position: absolute; left: 80px; right: 60px; top: 338px;
    height: 2px; background: var(--brand-red);
  }
  .phones { position: absolute; left: 80px; top: 352px; list-style: none; }
  .phones li {
    display: flex; align-items: center; gap: 14px;
    font-size: 28px; color: var(--ink); line-height: 40px;
  }
  .icon { width: 24px; height: 24px; flex: none; }

  .band { position: absolute; left: 0; bottom: 0; width: 900px; height: 514px; }

  .email {
    position: absolute; right: 60px; top: 352px;
    display: flex; align-items: center; gap: 12px;
    font-size: 28px; color: var(--ink);
  }
  .website {
    position: absolute; right: 60px; top: 430px;
    font-size: 28px; color: var(--paper-text); letter-spacing: .02em;
  }
</style>
</head>
<body>
<main class="sheet">
  <section class="card card--front" aria-label="Business card front">
    <svg class="band" viewBox="0 0 900 514" aria-hidden="true">
      <path d="M0,452 L410,452 C460,452 470,392 530,392 L900,392 L900,514 L0,514 Z" fill="var(--brand-red)"/>
      <path d="M0,466 L420,466 C470,466 480,410 540,410 L900,410 L900,514 L0,514 Z" fill="var(--card-black)"/>
    </svg>

    <div class="brand"><span class="brand__square"></span>Corvane Supplies</div>

    <div class="person">
      <p class="person__name">FULL NAME</p>
      <p class="person__role">CEO</p>
    </div>
    <div class="divider"></div>

    <ul class="phones">
      <li>
        <svg class="icon" viewBox="0 0 24 24" aria-hidden="true"><rect x="6" y="2" width="12" height="20" rx="2" fill="none" stroke="var(--brand-red)" stroke-width="2"/><circle cx="12" cy="18" r="1.3" fill="var(--brand-red)"/></svg>
        (000) 000 0000
      </li>
      <li>
        <svg class="icon" viewBox="0 0 24 24" aria-hidden="true"><path d="M6.6 10.8a15.1 15.1 0 0 0 6.6 6.6l2.2-2.2a1 1 0 0 1 1-.25 11.4 11.4 0 0 0 3.6.57 1 1 0 0 1 1 1V20a1 1 0 0 1-1 1A17 17 0 0 1 3 4a1 1 0 0 1 1-1h3.5a1 1 0 0 1 1 1c0 1.25.2 2.45.57 3.57a1 1 0 0 1-.25 1z" fill="var(--brand-red)"/></svg>
        (000) 000 0000
      </li>
    </ul>

    <p class="email">
      <svg class="icon" viewBox="0 0 24 24" aria-hidden="true"><rect x="2" y="5" width="20" height="14" fill="var(--brand-red)"/><path d="M2 5l10 8 10-8M2 19l8-7M22 19l-8-7" fill="none" stroke="#fff" stroke-width="1.5"/></svg>
      email@company.com
    </p>
    <p class="website">www.company.com</p>
  </section>

  <section class="card card--back" aria-label="Business card back">
    <div class="brand"><span class="brand__square"></span>Corvane Supplies</div>
  </section>
</main>
</body>
</html>
```